Menu revision for Korean Restaurant

I have posted the exact content in a word file that I would like to appear in the menu. Please apply to the template. I will be following up with prices shortly. I am in a hurry and not too picky. Thank you.

Make a menu with revisions.

Page 1: Cover Page
- Replace logo with new uploaded logo

Page 2:
Appetizers
Vegetarian Appetizers

Page 3:
BBQ Items

Page 4:
Signature Dishes

Page 5:
Bokkeum | Stir-Fry

Page 6:
Rice Bowls
Noodles
Hot Soup

Page 7:
Drinks

Target Market(s)

My customers

Industry/Entity Type

Restaurant

Requirements
Must have
• 1. Only use my menu content, template, and font.

```html
<!DOCTYPE html>
<html lang="en">
<head>
<meta charset="utf-8">
<title>Gaon Korean BBQ — Menu</title>
<link href="https://fonts.googleapis.com/css2?family=Russo+One&family=Oswald:wght@600&family=Noto+Serif:wght@400&family=Noto+Sans+KR:wght@500&display=swap" rel="stylesheet">
<style>
:root{
  --canvas:#ffffff;
  --page:#1f1e1c;
  --gold:#c9a54a;
  --gold-line:#8a7440;
  --red:#e0262b;
  --ink:#d9d3c4;
  --veg:#2e9e3e;
  --photo-hot:#c8471c;
  --photo-warm:#e08a3a;
  --photo-dark:#2a1a12;
}
*{box-sizing:border-box;margin:0;padding:0}
html,body{width:1200px;height:1200px;overflow:hidden;background:var(--canvas)}
.canvas{position:relative;width:1200px;height:1200px}
.page{position:absolute;width:269px;height:347px;background:var(--page);overflow:hidden}
.page > svg.frame{position:absolute;inset:0;width:269px;height:347px}
.title{position:absolute;top:18px;left:0;right:0;text-align:center;font-family:"Russo One",sans-serif;color:var(--red);font-size:12.5px;letter-spacing:1.8px}
.body{position:absolute;top:44px;bottom:26px;left:16px;right:16px;display:grid;grid-template-columns:1fr 1fr;column-gap:11px}
.col{display:flex;flex-direction:column;justify-content:space-between}
.item p{font-family:"Noto Serif","Noto Sans KR",serif;font-size:3.7px;line-height:1.4;color:var(--ink);text-align:justify}
.item b{font-family:"Oswald","Noto Sans KR",sans-serif;font-weight:600;color:var(--gold);letter-spacing:.2px}
.veg{display:block;width:4px;height:4px;border-radius:50%;background:var(--veg);margin:1px 0 0 auto}
.rule{position:relative;height:11px;flex:none}
.rule::before{content:"";position:absolute;left:0;right:0;top:5px;height:.5px;background:var(--gold-line);opacity:.7}
.rule::after{content:"";position:absolute;left:50%;top:0;width:11px;height:11px;margin-left:-5.5px;border-radius:50%;background:#5a4c2c;border:.6px solid var(--gold-line)}
.photo{position:relative;height:62px;flex:none;border-radius:1px;background:radial-gradient(ellipse 55% 45% at 52% 58%,var(--photo-warm),var(--photo-hot) 45%,var(--photo-dark) 100%)}
.photo span{position:absolute;top:3px;left:3px;font-family:"Oswald","Noto Sans KR",sans-serif;font-weight:600;font-size:3px;color:#fff;background:rgba(0,0,0,.55);padding:.8px 2px}
.footnote{position:absolute;bottom:13px;left:22px;font-family:"Noto Serif",serif;font-size:2.8px;color:var(--ink);display:flex;align-items:center;gap:4px}
.footnote i{display:inline-block;width:3.5px;height:3.5px;border-radius:50%;background:var(--veg)}
.cover-name{position:absolute;left:58px;top:150px;display:flex;align-items:center;gap:6px;font-family:"Russo One",sans-serif;color:var(--red);font-size:20px;letter-spacing:1px}
.cover-name .mark{width:26px;height:26px;background:var(--red)}
.cover-name small{font-size:9px;letter-spacing:.5px;margin-left:2px}
.section-title{font-family:"Russo One",sans-serif;color:var(--red);font-size:12px;letter-spacing:1.6px;text-align:center}
.sub{font-family:"Oswald",sans-serif;font-weight:600;color:var(--gold);font-size:3.4px;margin-top:2px}
.sub-text{font-family:"Noto Serif",serif;color:var(--ink);font-size:3.5px;line-height:1.4}
.drinks{position:absolute;font-family:"Noto Serif",serif;color:var(--ink);font-size:4px;line-height:5.8px;white-space:nowrap}
.drinks h3{font-family:"Oswald",sans-serif;font-weight:600;color:var(--gold);font-size:3.8px;line-height:5.8px;margin-top:2px}
.drinks-title{position:absolute;top:18px;left:28px;font-family:"Russo One",sans-serif;color:var(--red);font-size:12.5px;letter-spacing:1.8px}
</style>
</head>
<body>
<svg width="0" height="0" style="position:absolute">
  <defs>
    <symbol id="page-frame" viewBox="0 0 269 347">
      <g fill="none" stroke="#8a7440" stroke-width=".6" opacity=".75">
        <path d="M12 6H257V12H263V335H257V341H12V335H6V12H12Z"/>
        <rect x="3" y="3" width="7" height="7"/>
        <rect x="259" y="3" width="7" height="7"/>
        <rect x="3" y="337" width="7" height="7"/>
        <rect x="259" y="337" width="7" height="7"/>
      </g>
    </symbol>
  </defs>
</svg>

<main class="canvas">

  <!-- Cover -->
  <section class="page cover" style="left:30px;top:239px">
    <svg class="frame"><use href="#page-frame"/></svg>
    <div class="cover-name"><span class="mark"></span><span>GAON <small>Korean BBQ</small></span></div>
  </section>

  <!-- Appetizers -->
  <section class="page" style="left:319px;top:239px">
    <svg class="frame"><use href="#page-frame"/></svg>
    <h2 class="title">APPETIZERS</h2>
    <div class="body">
      <div class="col">
        <div class="item"><p><b>MANDU 군만두</b> Beef pot stickers fried and served with a side of house made soy-dipping sauce. $5.95</p></div>
        <i class="rule"></i>
        <div class="item"><p><b>MUL MANDU 물만두</b> Beef pot stickers boiled and served with a side of house made soy-dipping sauce. $5.95</p></div>
        <i class="rule"></i>
        <div class="item"><p><b>CHICKEN WINGS 닭날개</b> Fried chicken wings served with sweet and sour sauce. $8.95</p></div>
        <i class="rule"></i>
        <div class="item"><p><b>SPICY WINGS 닭날개</b> Fried and drizzled in Gaon's original wing sauce. $8.95</p></div>
        <i class="rule"></i>
        <div class="item"><p><b>SHRIMP TEMPURA 새우튀김</b> Jumbo shrimp fried in a crispy tempura batter with an assortment of fried onion, zucchini, and mushroom. $15.95</p></div>
        <i class="rule"></i>
        <div class="item"><p><b>FRIED CALAMARI 오징어튀김</b> Calamari fried in a light batter. $13.95</p></div>
        <i class="rule"></i>
        <div class="item"><p><b>HAEMUL PAJEON 해물파전</b> Fresh calamari, shrimp, scallops, mussels, and scallions in a Korean pancake. $15.95</p></div>
      </div>
      <div class="col">
        <div class="item"><p><b>VEGGIE MANDU 야채만두</b> Vegetable pot stickers fried and served with a side of house made soy-dipping sauce. $5.95</p><span class="veg"></span></div>
        <i class="rule"></i>
        <div class="item"><p><b>VEGGIE MUL MANDU 야채물만두</b> Vegetable pot stickers boiled and served with a side of house made soy-dipping sauce. $5.95</p><span class="veg"></span></div>
        <i class="rule"></i>
        <div class="item"><p><b>SWEET POTATO TEMPURA 고구마튀김</b> Crispy sweet potato slices fried in a light tempura batter. $6.95</p><span class="veg"></span></div>
        <i class="rule"></i>
        <div class="item"><p><b>VEGGIE TEMPURA 야채튀김</b> Vegetable medley of julienned carrot, onion, and zucchini fried in a crispy tempura batter. $6.95</p><span class="veg"></span></div>
        <i class="rule"></i>
        <div class="item"><p><b>MUSHROOM TEMPURA 버섯튀김</b> Fried button mushrooms. $5.95</p><span class="veg"></span></div>
        <i class="rule"></i>
        <div class="item"><p><b>PAJEON 파전</b> Pan fried green onion pancake. $12.95</p><span class="veg"></span></div>
        <i class="rule"></i>
        <div class="item"><p><b>HOBAK GOCHU JEON 호박고추전</b> Zucchini and Jalapeño pancake. $12.95</p><span class="veg"></span></div>
        <i class="rule"></i>
        <div class="item"><p><b>KIMCHI PAJEON 김치파전</b> Crispy kimchi and scallion pancake. $12.95</p><span class="veg"></span></div>
      </div>
    </div>
    <p class="footnote">*Item batter contains wheat flour &amp; eggs. <i></i> Vegetarian</p>
  </section>

  <!-- BBQ Items -->
  <section class="page" style="left:610px;top:239px">
    <svg class="frame"><use href="#page-frame"/></svg>
    <h2 class="title">BBQ ITEMS</h2>
    <div class="body">
      <div class="col">
        <div class="item"><p><b>*WANG GALBI 왕갈비</b> Hand crafted beef short rib marinated in a garlic soy &amp; rice wine marinade. $23.95</p></div>
        <i class="rule"></i>
        <div class="item"><p><b>*GAON GALBI 가온갈비</b> 3-bone beef short ribs marinated in a garlic soy &amp; rice wine marinade. $21.95</p></div>
        <i class="rule"></i>
        <div class="item"><p><b>*SAENG WANG GALBI 생왕갈비</b> Hand crafted beef short ribs. Non-marinated. $X.XX</p></div>
        <i class="rule"></i>
        <div class="item"><p><b>*SAENG GALBI 생갈비</b> 3-bone beef short ribs. Non-marinated. $23.95</p></div>
        <i class="rule"></i>
        <div class="item"><p><b>*SAENG DEUNG SHIM 생등심</b> Ribeye. Non-marinated. $27.95</p></div>
        <i class="rule"></i>
        <div class="item"><p><b>*JOOMULLUCK 주물럭</b> Sirloin. $21.95</p></div>
        <i class="rule"></i>
        <div class="item"><p><b>*CHADOL BAEGI 차돌박이</b> Thinly sliced black angus brisket. $18.95</p></div>
        <i class="rule"></i>
        <div class="item"><p><b>*HYUMITGUI 혀밑구이</b> Beef Tongue. $18.95</p></div>
        <i class="rule"></i>
        <div class="item"><p><b>*SAMGYEOPSAL 삼겹살</b> Pork Belly. $17.95</p></div>
      </div>
      <div class="col">
        <div class="item"><p><b>HEUKDWAEJI SAMGYEOPSAL 흑돼지삼겹살</b> Black Pig Pork Belly. $18.95</p></div>
        <i class="rule"></i>
        <div class="item"><p><b>*HANG JUNG SAL 항정살</b> Pork Jowl. $18.95</p></div>
        <i class="rule"></i>
        <div class="item"><p><b>*SAEWOO 새우</b> Shrimp. $18.95</p></div>
        <i class="rule"></i>
        <div class="item"><p><b>*JJUGGUMI 쭈꾸미</b> Baby Octopus. $18.95</p></div>
        <i class="rule"></i>
        <div class="item"><p><b>*OJINGUH 오징어</b> Calamari. $18.95</p></div>
        <i class="rule"></i>
        <div class="item"><p><b>*HONGHAB 홍합</b> Mussel. $18.95</p></div>
        <i class="rule"></i>
        <div class="item"><p><b>*YACHAE GUI 야채구이</b> Assorted Vegetables. $12.95</p><span class="veg"></span></div>
        <i class="rule"></i>
        <div class="item"><p><b>*BULGOGI 불고기</b> Tenderloin/Sirloin marinated in garlic-soy marinate. $12.95</p></div>
        <i class="rule"></i>
        <div class="item"><p><b>*DAK BULGOGI 닭불고기</b> Boneless chicken breast. Marinated in teriyaki sauce. $19.95</p></div>
        <i class="rule"></i>
        <div class="item"><p><b>*DWAEJI BULGOGI 돼지불고기</b> Pork loin marinated with house blend chili pepper paste. $19.95</p></div>
      </div>
    </div>
    <p class="footnote">*Item batter contains wheat flour &amp; eggs. <i></i> Vegetarian</p>
  </section>

  <!-- Signature Dishes -->
  <section class="page" style="left:898px;top:239px">
    <svg class="frame"><use href="#page-frame"/></svg>
    <h2 class="title">SIGNATURE DISHES</h2>
    <div class="body">
      <div class="col">
        <div class="item"><p><b>DWAEJI BOSSAM 돼지보쌈</b> Braised pork belly wraps accompanied with a spicy gochu &amp; oyster-pureed radish salad. Served with fresh garlic &amp; jalapeño slices, a side of salty shrimp sauce, and a side of house made ssam-jang soybean paste with choice of boiled Napa cabbage wrap or fresh lettuce wrap. $25.95</p></div>
        <div class="photo" role="img" aria-label="Photo of glazed braised pork on a white plate"><span>DWAEJI BOSSAM 돼지보쌈</span></div>
        <i class="rule"></i>
        <div class="item"><p><b>*YOOK-HWE 육회</b> Raw sesame steak tartar &amp; egg yolk. Julienned strips of premium beef seasoned and dressed with Korean pear, garlic, &amp; pine nuts. $18.95</p></div>
        <i class="rule"></i>
        <div class="item"><p><b>PORK KATSU 돈까스</b> Pork loin breaded in seasoned panko crust &amp; deep-fried. Dressed with bold katsu sauce and served with radish condiments. $13.95</p></div>
        <i class="rule"></i>
        <div class="item"><p><b>CHICKEN KATSU 치킨까스</b> Chicken breast breaded in seasoned panko crust &amp; deep-fried. Dressed with bold katsu sauce and served with radish condiments. $13.95</p></div>
      </div>
      <div class="col">
        <div class="item"><p><b>SWEET &amp; SOUR PORK 탕수육</b> Pork tenderloin fried in a light batter. Served with fresh vegetables and pineapples. Drizzled with house made sweet &amp; sour sauce. $15.95</p></div>
        <i class="rule"></i>
        <div class="item"><p><b>SWEET &amp; SOUR CHICKEN 깐풍기</b> Tender pieces of all white chicken breast fried in a light batter. Served with fresh vegetables and pineapples. Drizzled with house made sweet &amp; sour sauce. $15.95</p></div>
        <i class="rule"></i>
        <div class="item"><p><b>BULGOGI-IN-A-BOWL 뚝배기불고기</b> Bulgogi, vermicelli, enoki, button mushrooms, scallions, onions, &amp; carrot garnish all in one bowl &amp; filled to the rim with a hearty bulgogi broth. $16.95</p></div>
        <i class="rule"></i>
        <div class="item"><p><b>GOBCHANG GUI 곱창구이</b> Sizzling beef chitterlings with tripe and vegetable medley spiced with wild sesame and red pepper oil. $17.95</p></div>
        <i class="rule"></i>
        <div class="item"><p><b>CHUB MACKEREL 고등어구이</b> Whole bone-in silver belly chub mackerel salted and seared. $23.95</p></div>
        <div class="photo" role="img" aria-label="Photo of a plated signature dish"><span>CHUB MACKEREL 고등어구이</span></div>
      </div>
    </div>
    <p class="footnote">*Item batter contains wheat flour &amp; eggs. <i></i> Vegetarian</p>
  </section>

  <!-- Bokkeum | Stir-Fry -->
  <section class="page" style="left:319px;top:609px">
    <svg class="frame"><use href="#page-frame"/></svg>
    <h2 class="title">BOKKEUM | STIR-FRY</h2>
    <div class="body">
      <div class="col">
        <div class="item"><p><b>JEYUK BOKKEUM 제육볶음</b> Pork, onions, scallions, mushrooms and jalapeños stir-fried in a spicy red garlic sauce. $15.95</p></div>
        <div class="photo" role="img" aria-label="Photo of spicy pork stir-fry on a white plate"><span>DWAEJI BOSSAM 돼지보쌈</span></div>
        <i class="rule"></i>
        <div class="item"><p><b>DUBU BOKKEUM 두부볶음</b> Fried tofu cubes, zucchini, carrots, onions, and mushrooms stir-fried in a red chili sauce. $13.95</p><span class="veg"></span></div>
        <i class="rule"></i>
        <div class="item"><p><b>KIMCHI BOKKEUM 김치볶음</b> Pork, kimchi, rice cakes, scallions, onions, and fresh tofu. $15.95</p></div>
        <div class="photo" role="img" aria-label="Photo of kimchi stir-fry on a white plate"><span>SAMPLE TEXT 글씨</span></div>
      </div>
      <div class="col">
        <div class="item"><p><b>HAEMUL BOKKEUM 해물볶음</b> Jumbo shrimp, scallops, mussels, calamari, octopus, zucchini, carrots, onions, scallions, mushrooms, and jalapeños. $17.95</p></div>
        <i class="rule"></i>
        <div class="item"><p><b>SAMGYUPSAL BOKKEUM 삼겹살볶음</b> Pork belly, zucchini, onions, scallions stir-fried in a spicy gochu wine sauce. $15.95</p></div>
        <i class="rule"></i>
        <div class="item"><p><b>OJINGEO BOKKEUM 오징어볶음</b> Fresh calamari stir-fried with carrots, zucchini, mushrooms, onions and scallions in a hot and spicy chili sauce. $15.95</p></div>
        <div class="photo" role="img" aria-label="Photo of calamari stir-fry on a white plate"><span>OJINGEO BOKKEUM 오징어볶음</span></div>
        <i class="rule"></i>
        <div class="item"><p><b>NAKJI BOKKEUM 낙지볶음</b> Fresh octopus stir-fried with carrots, zucchini, mushrooms, onions, and scallions in a hot and spicy chili sauce. $15.95</p></div>
        <i class="rule"></i>
        <div class="item"><p><b>JJUGGUMI SAMGYUPSAL 쭈꾸미삼겹살</b> Spicy pork belly and baby octopus. $18.95</p></div>
      </div>
    </div>
    <p class="footnote">*Item batter contains wheat flour &amp; eggs. <i></i> Vegetarian</p>
  </section>

  <!-- Rice Bowls / Noodles / Hot Soup -->
  <section class="page" style="left:612px;top:609px">
    <svg class="frame"><use href="#page-frame"/></svg>
    <h2 class="title">RICE BOWLS</h2>
    <div class="body" style="top:44px;bottom:auto;height:100px">
      <div class="col" style="justify-content:flex-start">
        <div class="item"><p><b>*YUKHWE BIBIMBAP 육회비빔밥</b> Raw beef tartar &amp; egg yolk on rice with a colorful spread of spinach, carrots, bean sprouts, soybean sprouts, shiitake mushrooms, zucchini, and radish. Topped with garlic and pine nuts &amp; served with a side of house-made gochujang &amp; bowl of rice.</p></div>
        <div style="display:grid;grid-template-columns:1fr 1fr;gap:4px;margin-top:8px">
          <div><p class="sub">DIRECTIONS:</p><p class="sub-text">1. Add gochujang<br>2. Mix</p></div>
          <div><p class="sub">CHOOSE CENTERPIECE:</p><p class="sub-text">Bulgogi (original) or<br>Chicken: $xx.xx<br>Kimchi &amp; Pork: $xx.xx<br>Seafood: $xx.xx</p></div>
        </div>
      </div>
      <div class="col" style="justify-content:flex-start;gap:6px">
        <div class="item"><p><b>*DOLSOT BIBIMBAP 돌솥비빔밥</b> Sizzling hot stone bowl bibimbap. Individually marinated spinach, carrots, bean sprouts, soybean sprouts, shiitake mushrooms, zucchini, and radish topped with choice of fried egg or raw egg. Served with a side of house-made gochujang sauce.</p></div>
        <div class="photo" style="height:50px" role="img" aria-label="Photo of a stone bowl bibimbap"><span>*DOLSOT BIBIMBAP 돌솥비빔밥</span></div>
      </div>
    </div>
    <i class="rule" style="position:absolute;left:16px;right:16px;top:144px"></i>
    <div class="body" style="top:160px;bottom:26px">
      <div class="col" style="justify-content:flex-start;gap:7px">
        <h2 class="section-title">NOODLES</h2>
        <div class="item"><p><b>MUL NAENG MYUN 물냉면</b> Beef brisket, pickled radish, cucumber slices, jalapeños, and hard-boiled egg layered on top of thin buckwheat noodles in icy beef broth. $xx.xx</p></div>
        <i class="rule"></i>
        <div class="item"><p><b>BIBIM NAENG MYUN 비빔냉면</b> Pickled radish, cucumber slices, jalapeños, scallions, and hard-boiled egg atop a mound of sweet &amp; spicy buckwheat noodles. $xx.xx</p></div>
        <div class="photo" style="height:56px" role="img" aria-label="Photo of spicy cold buckwheat noodles"><span>BIBIM NAENG MYUN 비빔냉면</span></div>
      </div>
      <div class="col" style="justify-content:flex-start;gap:7px">
        <h2 class="section-title">HOT SOUP</h2>
        <div class="item"><p><b>*SOON DUBU CHIGAE 순두부찌개</b> Soft tofu stew with mushrooms, egg, and choice of protein in boiling spicy chili oil broth.<br>Vegetarian $xx.xx &nbsp; Beef, Chicken or Pork $xx.xx<br>Seafood $xx.xx</p></div>
        <i class="rule"></i>
        <div class="item"><p><b>KIMCHI CHIGAE 김치찌개</b> Kimchi, pork, tofu, fish cake, scallions, mushrooms and spicy pepper flakes in boiling kimchi broth. $xx.xx</p></div>
        <i class="rule"></i>
        <div class="item"><p><b>GALBI TANG 갈비탕</b> Beef short rib soup with radishes, mushrooms, scallions, vermicelli noodles. $xx.xx</p></div>
        <i class="rule"></i>
      </div>
    </div>
    <p class="footnote">*Item batter contains wheat flour &amp; eggs. <i></i> Vegetarian</p>
  </section>

  <!-- Drinks -->
  <section class="page" style="left:900px;top:609px">
    <svg class="frame"><use href="#page-frame"/></svg>
    <h2 class="drinks-title">DRINKS</h2>
    <div class="drinks" style="left:28px;top:38px">
      <h3>DRAFT</h3>
      Northfield Amber $7.00<br>Northfield Pale Ale<br>Ridgeline EPA $6.00<br>Hanul Lager $8.00<br>Pinecrest Light $5.00<br>Riverbend Unrated $7.00<br>Belmonte Pils $7.00
      <h3>BOTTLES</h3>
      Haneul Korean Pale Lager $6.00<br>Golden Lotus $6.00<br>Mekong Lager $6.00<br>Eastport Lager $6.00<br>Sakuragi $6.00<br>Tyneside Brown $6.00<br>Marlow Gluten Free Ginger Beer $7.00<br>Tres Palmas $6.00<br>Open Road Amber $7.00<br>Orchard Hill $6.00<br>Polder Lager $6.00
      <h3>LIQUORS</h3>
      Stillwater Bourbon $16.00<br>Maison Ravel VS $9.00
      <h3>WHITE WINE</h3>
      Sunridge (Viognier) $16<br>The Curio (Furmint) $12<br>Domaine Lune Bordeaux (Rosé) $10<br>Colle Alto (Pinot Grigio) $17<br>Maison Clair (Imperial Brut) $46<br>Oakhaven Napa Valley (Chardonnay) $14<br>Cedar Bluff (Sauvignon Blanc) $11<br>Casa Fiora (Moscato) $8<br>Tidewater (Sauvignon Blanc) $17<br>Canyon Bend (Riesling) $9<br>Ashby Ranch (Sauvignon Blanc) $11
      <h3>RED WINE</h3>
      Château Belrive (Red Bordeaux) $11<br>Château Beaulac 7 $14<br>Andes Peak Reserve (Malbec) $10<br>Pampa Sur (Malbec) $12<br>Cypress Ridge (Pinot Noir) $15<br>Seaside Hollow (Pinot Noir) $16<br>Prairie Run (Cabernet Sauvignon) $17
    </div>
    <div class="drinks" style="left:144px;top:19px">
      Regal Crest Apple $8.00<br>Regal Crest $7.00<br>Regal Crest Sp. Reserve $14.00<br>Regal Crest XR $36.00<br>Highland Stride Black Label $8.50<br>Highland Stride Blue Label $80 / $1200<br>Thistle Glen 12yr $9.00<br>Agave Luna Reposado $16.00<br>Dewdrop Soju 750ml $4.00 / $38<br>Ben Arran 12yr $12.00<br>Ben Arran 18yr $28.00<br>Ben Arran 21yr $75.00 / $1500.00<br>Larkspur Gin $9.50<br>Maison Ravel XO $55.00 / $800.00<br>Northmoor 18yr $45.00<br>Two Crowns Scotch $6.00<br>Highland Stride Platinum $40.00 / $600.00<br>Highland Stride Red Label $6.00<br>Tennessee Hollow $6.00<br>Emerald Coast Irish Whiskey $7.00<br>Fjord Spring Water $5.00<br>Maison Delorme Vsop $11.00<br>Vine Crest Vodka $8.00<br>Casa Sol Blanco $14.00<br>Silver Swan Vodka $8.00<br>Sierra Alta Tequila $7.00<br>Indigo Gin $7.00<br>Orangerie Liqueur $8.50<br>Mount Kiso 12yr $36.00<br>Harmonia 12yr $36.00<br>Ember Shot $5.00<br>Palm Cove $5.00<br>Plata Fina Silver $9.00<br>Almond Grove Amaretto $5.00<br>Pink Lark Blue $7.00<br>Pink Lark Vodka $5.00<br>Canal Street $5.00<br>Volga Blue $6.00<br>Iron Hawk 101 $7.00<br>Forest Herbal $6.00<br>Kentucky Gate $6.00<br>Redwax Bourbon $8.00<br>Windmill Vodka $8.00<br>Stone Hollow $11.00<br>Frost Peppermint $6.00<br>Magnolia Liqueur $6.00<br>Greenbridge Gin $7.00<br>Shannon Mist $7.00<br>Vine Crest Peach $8.00<br>Vine Crest Red Berry $8.00<br>Nordic Citron $6.00<br>Tower Guard Gin $6.00
    </div>
  </section>

</main>
</body>
</html>
```